401K Retirement Plan Consultant

Professional & clean lines - not overly busy. We offer two services - 401k administration and HSA administration. Based on the outskirts of Charlotte NC. Communicate the services we offer along with the financial institutions that we work with. Mixture of icons and people pictures.

Current website - tvh401k.com,
It is presently very amateurish.

```html
<!DOCTYPE html>
<html lang="en">
<head>
<meta charset="utf-8">
<title>TVH401K Employee Benefits</title>
<link href="https://fonts.googleapis.com/css2?family=Archivo+Black&family=Lato:wght@400;700&family=Montserrat:wght@500;600;700&display=swap" rel="stylesheet">
<style>
:root{
  --blue:#1414e0;
  --blue-deep:#0a0ad0;
  --ink:#111;
  --body:#333;
  --white:#fff;
  --footer:#202020;
  --muted:#ddd;
}
*{box-sizing:border-box;margin:0;padding:0}
html,body{width:1200px;height:4135px;overflow:hidden}
body{position:relative;font-family:'Lato',sans-serif;color:var(--ink);background:var(--white)}
.abs{position:absolute}
a{color:inherit;text-decoration:none}

/* top bar */
.topbar{left:0;top:0;width:1200px;height:68px;background:var(--blue);color:var(--white);font-family:'Montserrat',sans-serif}
.topbar .label{position:absolute;top:6px;font-size:14px;font-weight:700}
.topbar .value{position:absolute;top:34px;font-size:14px;display:flex;align-items:center;gap:8px}
.ic-round{width:28px;height:28px;border-radius:50%;background:var(--white);display:inline-flex;align-items:center;justify-content:center}
.socials{display:flex;gap:12px}
.social{width:30px;height:30px;border-radius:50%;border:2px solid var(--white);background:transparent}
.topbar .socials{position:absolute;right:110px;top:19px}

/* nav */
.nav{left:0;top:68px;width:1200px;height:100px;background:var(--white)}
.brand{position:absolute;font-family:'Montserrat',sans-serif;color:var(--ink)}
.brand .name{font-size:34px;font-weight:600;letter-spacing:1px;line-height:1}
.brand .tag{font-size:11px;letter-spacing:2px;margin-top:2px}
.nav .brand{left:110px;top:26px}
.menu{position:absolute;left:336px;top:42px;display:flex;gap:35px;font-size:16px;color:#222}
.btn{display:inline-flex;align-items:center;justify-content:center;border-radius:30px;font-family:'Montserrat',sans-serif;font-weight:700;text-transform:uppercase}
.btn-blue{background:var(--blue);color:var(--white)}
.btn-white{background:var(--white);color:#000}
.nav .btn{position:absolute;left:943px;top:32px;width:145px;height:42px;font-size:15px}

/* hero */
.hero{left:0;top:168px;width:1200px;height:644px;background:linear-gradient(100deg,#4f6572 0%,#3c7fa6 35%,#8fb3c9 60%,#c9c3b4 100%)}
.hero h1{position:absolute;left:108px;top:158px;font-family:'Archivo Black',sans-serif;font-size:52px;line-height:62px;color:var(--white);text-transform:uppercase}
.hero h1 .hl{color:var(--blue)}
.hero p{position:absolute;left:108px;top:355px;width:500px;font-size:14.5px;line-height:28px;color:var(--white)}
.hero .btn{position:absolute;left:108px;top:437px;width:145px;height:42px;font-size:15px}

/* headings */
.sec-title{position:absolute;left:0;width:1200px;text-align:center;font-family:'Archivo Black',sans-serif;font-size:37px;text-transform:uppercase}
.sec-title span{border-bottom:4px solid currentColor;padding-bottom:2px}
.sec-sub{position:absolute;left:0;width:1200px;text-align:center;font-family:'Montserrat',sans-serif;font-size:24px}

/* about */
.about-lead{top:935px;font-size:23px;text-transform:uppercase}
.about-text{position:absolute;left:160px;top:993px;width:880px;text-align:center;font-size:14.5px;line-height:28px;color:var(--body)}
.about-btn{position:absolute;left:527px;top:1106px;width:146px;height:42px;font-size:15px}

/* services */
.services-band{left:0;top:1235px;width:1200px;height:509px;background:linear-gradient(90deg,#2b2be8,#1b1bd8 50%,#3535e6)}
.svc-card{position:absolute;top:1453px;width:455px;height:488px;background:var(--white);border-radius:6px;box-shadow:0 2px 12px rgba(0,0,0,.18)}
.svc-photo{position:absolute;left:10px;top:8px;width:435px;height:220px;border-radius:6px}
.svc-icon{position:absolute;left:187px;top:196px;width:76px;height:76px;border-radius:50%;background:var(--blue);border:5px solid var(--white);display:flex;align-items:center;justify-content:center}
.svc-card h3{position:absolute;top:297px;left:0;width:100%;text-align:center;font-family:'Montserrat',sans-serif;font-weight:700;font-size:24px}
.svc-card p{position:absolute;top:336px;left:40px;width:375px;text-align:center;font-size:14.5px;line-height:28px;color:var(--body)}
.svc-card .btn{position:absolute;left:165px;top:434px;width:124px;height:33px;font-size:13px}

/* other services strip */
.strip{left:0;top:2133px;width:1200px;height:300px;background:var(--white)}
.slice{position:absolute;top:0;height:300px;font-family:'Archivo Black',sans-serif;color:var(--white);font-size:24px}
.slice .lbl{position:absolute;top:12px}

/* features */
.features{left:0;top:2521px;width:1200px;height:795px;background:var(--blue)}
.feat{position:absolute;width:295px;height:231px;border:3px solid var(--white);color:var(--white)}
.feat .ficon{position:absolute;left:18px;top:-30px;width:56px;height:50px;background:var(--blue);display:flex;align-items:center;justify-content:center}
.feat h4{position:absolute;left:13px;top:37px;font-family:'Montserrat',sans-serif;font-weight:700;font-size:18px}
.feat p{position:absolute;left:13px;top:76px;width:272px;font-size:14px;line-height:25.6px}
.features .btn{position:absolute;left:527px;top:690px;width:146px;height:40px;font-size:15px;color:var(--blue-deep)}

/* partners */
.partner{position:absolute;top:3540px;width:186px;height:104px;background:var(--white);box-shadow:0 2px 10px rgba(0,0,0,.12);display:flex;align-items:center;justify-content:center;gap:8px;font-family:'Montserrat',sans-serif;font-weight:600;font-size:20px;color:#333}
.partner .dot{width:14px;height:14px;border-radius:50%;background:#9aa0aa}

/* footer */
.footer{left:0;top:3729px;width:1200px;height:406px;background:var(--footer);color:var(--white);font-family:'Montserrat',sans-serif}
.footer .brand{left:110px;top:90px;color:var(--white)}
.footer .about{position:absolute;left:110px;top:155px;width:210px;font-family:'Lato',sans-serif;font-size:14.5px;line-height:28px}
.fcol{position:absolute;top:85px}
.fcol h5{font-size:19px;font-weight:700;letter-spacing:1.5px;margin-bottom:14px}
.fcol li{list-style:none;font-size:17px;line-height:31px;letter-spacing:.5px}
.footer .follow{position:absolute;left:890px;top:208px;font-size:19px;font-weight:700;letter-spacing:1.5px}
.footer .socials{position:absolute;left:890px;top:245px}
.footer .rule{position:absolute;left:72px;top:328px;width:1056px;height:1px;background:#888}
.footer .copy{position:absolute;top:357px;left:0;width:1200px;text-align:center;font-size:15px;letter-spacing:1px}
.footer .copy b{font-weight:700}
</style>
</head>
<body>

<header class="abs topbar">
  <div class="label" style="left:110px">TELEPHONE:</div>
  <div class="value" style="left:110px">
    <span class="ic-round"><svg width="16" height="16" viewBox="0 0 24 24"><path d="M6.6 10.8a15 15 0 0 0 6.6 6.6l2.2-2.2c.3-.3.7-.4 1-.2 1.1.4 2.3.6 3.6.6.6 0 1 .4 1 1V20c0 .6-.4 1-1 1A17 17 0 0 1 3 4c0-.6.4-1 1-1h3.5c.6 0 1 .4 1 1 0 1.2.2 2.4.6 3.6.1.3 0 .7-.2 1z" fill="#1414e0"/></svg></span>
    1 704 555 0142
  </div>
  <div class="label" style="left:507px">E-MAIL:</div>
  <div class="value" style="left:507px">
    <span class="ic-round"><svg width="16" height="16" viewBox="0 0 24 24"><rect x="3" y="6" width="18" height="12" rx="1" fill="none" stroke="#1414e0" stroke-width="2"/><path d="M3 7l9 6 9-6" fill="none" stroke="#1414e0" stroke-width="2"/></svg></span>
    Service@tvh401k.com
  </div>
  <div class="socials" aria-label="Social links">
    <span class="social"></span><span class="social"></span><span class="social"></span><span class="social"></span><span class="social"></span>
  </div>
</header>

<nav class="abs nav">
  <div class="brand"><div class="name">TVH401K</div><div class="tag">EMPLOYEE BENEFITS</div></div>
  <div class="menu"><a>Home</a><a>About Us</a><a>Our Services</a><a>Our Partners</a><a>Contact Us</a></div>
  <a class="btn btn-blue">Get Started</a>
</nav>

<section class="abs hero" role="img" aria-label="Photo of a smiling family of four on a seaside cliff path">
  <h1>Welcome to&nbsp; TVH<br><span class="hl">401K</span> Employee<br>Benefits</h1>
  <p>Lorem ipsum dolor sit amet, consectetur adipiscing elit, sed do eiusmod tempor incididunt ut labore et dolore magna aliqua.</p>
  <a class="btn btn-white">Contact</a>
</section>

<h2 class="sec-title" style="top:868px"><span>About Us</span></h2>
<div class="sec-sub about-lead">We are glad to welcome you to our company!</div>
<p class="about-text">Located in the heart of Cedar Cove, SC, TVH has been providing employee benefits since 1987.&nbsp; We specialize in small companies normally with les than 150 employees. TVH's retirement plan solutions are designed to serve a broad range of clients and offer the advantages of large-plan pricing to small&nbsp; employer-sponsored retirement plans.</p>
<a class="btn btn-blue about-btn">Contact</a>

<section class="abs services-band" role="img" aria-label="Blue-tinted photo of a business meeting"></section>
<h2 class="sec-title" style="top:1310px;color:var(--white)"><span>Our Services</span></h2>
<div class="sec-sub" style="top:1372px;color:var(--white)">TVH has been providing employee benefit services since 1987.</div>

<article class="svc-card" style="left:110px">
  <div class="svc-photo" role="img" aria-label="Photo of a woman working on a laptop in an office" style="background:linear-gradient(135deg,#3a3530,#7a716a 50%,#c9c2b8)"></div>
  <div class="svc-icon"><svg width="34" height="34" viewBox="0 0 24 24" fill="none" stroke="#fff" stroke-width="1.6"><circle cx="12" cy="7" r="3.5"/><path d="M5 21v-3a7 7 0 0 1 14 0v3z"/><rect x="8" y="15" width="8" height="5"/></svg></div>
  <h3>401K ADMINISTRATION</h3>
  <p>Lorem ipsum dolor sit amet, consectetur adipiscing elit, sed do eiusmod tempor incididunt ut labore et dolore magna aliqua. Ut enim ad minim veniam</p>
  <a class="btn btn-blue">Click Here</a>
</article>

<article class="svc-card" style="left:634px">
  <div class="svc-photo" role="img" aria-label="Photo of a hand touching a glowing HSA interface" style="background:radial-gradient(circle at 40% 30%,#b89760,#4a3c2a 45%,#1c1814)"></div>
  <div class="svc-icon"><svg width="34" height="34" viewBox="0 0 24 24" fill="none" stroke="#fff" stroke-width="1.6"><circle cx="12" cy="12" r="8"/><path d="M12 8v8M8 12h8"/></svg></div>
  <h3>HSA ADMINISTRATION</h3>
  <p>Lorem ipsum dolor sit amet, consectetur adipiscing elit, sed do eiusmod tempor incididunt ut labore et dolore magna aliqua. Ut enim ad minim veniam</p>
  <a class="btn btn-blue">Click Here</a>
</article>

<h2 class="sec-title" style="top:1998px"><span>Other Services</span></h2>
<div class="sec-sub" style="top:2064px">Lorem ipsum dolor sit amet, consectetur adipiscing elit</div>

<section class="abs strip">
  <div class="slice" role="img" aria-label="Photo of a money sack with coins" style="left:0;width:260px;clip-path:polygon(0 0,100% 0,70% 100%,0 100%);background:linear-gradient(160deg,#cfc7bb,#8a7350)"><span class="lbl" style="left:102px">HSA</span></div>
  <div class="slice" role="img" aria-label="Photo of a young woman with her elderly mother" style="left:176px;width:340px;clip-path:polygon(24% 0,100% 0,75% 100%,0 100%);background:linear-gradient(160deg,#b8aca0,#e4dcd2)"><span class="lbl" style="left:120px">COBRA</span></div>
  <div class="slice" role="img" aria-label="Blue-tinted photo of business professionals" style="left:432px;width:340px;clip-path:polygon(25% 0,100% 0,76% 100%,0 100%);background:linear-gradient(160deg,#3c3cc8,#1a1adf)"><span class="lbl" style="left:90px;top:215px;text-align:center;line-height:30px">DEPENDENT<br>CARE</span></div>
  <div class="slice" role="img" aria-label="Photo of a doctor with an elderly patient" style="left:688px;width:350px;clip-path:polygon(0 0,76% 0,100% 100%,12% 100%);background:linear-gradient(160deg,#7b8a85,#d9dde0)"><span class="lbl" style="left:142px">HRA</span></div>
  <div class="slice" role="img" aria-label="Photo of a pink piggy bank" style="left:950px;width:250px;clip-path:polygon(0 0,100% 0,100% 100%,18% 100%);background:linear-gradient(160deg,#d8d4d0,#e8c0c0)"><span class="lbl" style="left:95px">FSA</span></div>
</section>

<section class="abs features">
  <div class="feat" style="left:110px;top:98px">
    <div class="ficon"><svg width="44" height="40" viewBox="0 0 24 24" fill="#fff"><path d="M2 11L22 3l-5 18-5-6-4 4v-6z"/></svg></div>
    <h4>Open Architecture Platform</h4>
    <p>All of our plans are designed using an open architecture investment platform. This allows for a myriad of investment choices&nbsp; for its participants.&nbsp; Instead of offering a set group of funds.</p>
  </div>
  <div class="feat" style="left:452px;top:98px">
    <div class="ficon"><svg width="50" height="40" viewBox="0 0 30 20" fill="#fff"><circle cx="15" cy="5" r="4"/><circle cx="6" cy="7" r="3"/><circle cx="24" cy="7" r="3"/><path d="M8 20a7 7 0 0 1 14 0zM0 20a6 6 0 0 1 9-5l-1 5zM30 20a6 6 0 0 0-9-5l1 5z"/></svg></div>
    <h4>Employee Education</h4>
    <p>TVH401k provides participants with group educational meetings to discuss plan features, investment options, which helps your participants be better prepared for retirement.</p>
  </div>
  <div class="feat" style="left:792px;top:98px">
    <div class="ficon"><svg width="34" height="42" viewBox="0 0 18 24" fill="#fff"><path d="M0 0h12l6 6v18H0z"/><path d="M4 11h10M4 15h10M4 19h10" stroke="#1414e0" stroke-width="1.6"/></svg></div>
    <h4>IRS 5500 &amp; 1099-R's</h4>
    <p>ERISA Form 5500 was created so the government can assess the financial condition, investments, and operations of all employee benefits plans.&nbsp; They are prepared annually along with 1099-R</p>
  </div>
  <div class="feat" style="left:110px;top:395px">
    <div class="ficon"><svg width="54" height="36" viewBox="0 0 30 20" fill="#fff"><circle cx="15" cy="5" r="4"/><circle cx="5" cy="14" r="4"/><circle cx="25" cy="14" r="4"/><path d="M15 5L5 14M15 5l10 9" stroke="#fff" stroke-width="2"/></svg></div>
    <h4>Non-Discrimination Testing</h4>
    <p>Nondiscrimination tests ensure that highly compensated employees do not take substantially greater advantage of this tax savings than lower-paid employees.</p>
  </div>
  <div class="feat" style="left:452px;top:395px">
    <div class="ficon"><svg width="42" height="42" viewBox="0 0 24 24" fill="#fff"><circle cx="12" cy="12" r="7"/><g stroke="#fff" stroke-width="3"><path d="M12 1v4M12 19v4M1 12h4M19 12h4M4 4l3 3M17 17l3 3M20 4l-3 3M7 17l-3 3"/></g><path d="M12 9v6M9 12h6" stroke="#1414e0" stroke-width="2"/></svg></div>
    <h4>HSA Administration</h4>
    <p>An HSA is a unique tax-advantaged account that can be used for paying or reimbursing qualified medical expenses for an individual, spouse or family. To be eligible you must have a high deductible</p>
  </div>
  <div class="feat" style="left:792px;top:395px">
    <div class="ficon"><svg width="46" height="46" viewBox="0 0 24 24" fill="#fff"><circle cx="14" cy="6" r="4.5"/><path d="M6 22a8 8 0 0 1 16 0z"/><circle cx="6" cy="17" r="4" stroke="#1414e0" stroke-width="1.5"/></svg></div>
    <h4>COBRA Administration</h4>
    <p>This is the federal law that provides many workers with the right to continue coverage in a group health plan. This federal law applies to employers with 20 or more employees, including</p>
  </div>
  <a class="btn btn-white">View All</a>
</section>

<h2 class="sec-title" style="top:3391px"><span>Our Partners</span></h2>
<div class="sec-sub" style="top:3456px">Lorem ipsum dolor sit amet, consectetur adipiscing elit</div>

<div class="partner" style="left:22px">Northvale</div>
<div class="partner" style="left:213px">Brightpath</div>
<div class="partner" style="left:408px">Keystone</div>
<div class="partner" style="left:604px"><span class="dot"></span>Harbor Funds</div>
<div class="partner" style="left:799px">Summit Trust</div>
<div class="partner" style="left:995px;font-size:18px"><span class="dot"></span>Meridian Group</div>

<footer class="abs footer">
  <div class="brand"><div class="name">TVH401K</div><div class="tag">EMPLOYEE BENEFITS</div></div>
  <p class="about">Lorem ipsum dolor sit amet, consectetur adipiscing elit, sed do eiusmod tempor incididunt ut labore et dolore</p>
  <div class="fcol" style="left:373px"><h5>ABOUT COMPANY</h5><ul><li>Home</li><li>About us</li><li>Our Services</li><li>Our Partners</li><li>Contact Us</li></ul></div>
  <div class="fcol" style="left:660px"><h5>QUICK LINKS</h5><ul><li>Privacy Policy</li><li>Terms of Use</li><li>Site Map</li><li>Cookies policy</li><li>Support</li></ul></div>
  <div class="fcol" style="left:890px"><h5>OUR SERVICES</h5><ul><li>401k administration</li><li>HSA administration</li></ul></div>
  <div class="follow">FOLLOW US</div>
  <div class="socials" aria-label="Social links">
    <span class="social"></span><span class="social"></span><span class="social"></span><span class="social"></span><span class="social"></span>
  </div>
  <div class="rule"></div>
  <div class="copy">Copyright © 2024&nbsp; <b>TVH401K EMPLOYEE BENEFITS.</b> All Rights Reserved</div>
</footer>

</body>
</html>
```